Pop up exhibition stand 2000mm (H) x 800mm (W)

I would like a simple pop up banner stand for an exhibition.

We need a pop up banner stand design for 'Brindle Forge Services'

the size is 2000mm(H) x 800mm (W)

Ad copy as follows :

[Brindle Forge logo]

From Sheet Metal To Large Sand Castings

Our Capacity and Rapid Quenching drop bottom ovens deliver precise processing.
We also serve the leading names in aerospace, automotive and advanced engineering.

Visit www.brindleforge-example.co.uk/ or call us Tel: +44 (0)1632 960318

[Put the crafted across the shires logo here, also include the text member somewhere close]

check on their website for other ideas that can help you with this project.

Target Market(s)

will be used at a trade show

Requirements
Nice to have
• modern design for UK manufacturing business

```html
<!DOCTYPE html>
<html lang="en">
<head>
<meta charset="utf-8">
<title>Brindle Forge Services – Exhibition Pop-up Banner</title>
<link href="https://fonts.googleapis.com/css2?family=Open+Sans:wght@400;600;700&display=swap" rel="stylesheet">
<style>
  :root {
    --red: #e2231a;
    --red-deep: #c8161d;
    --orange: #f26a3a;
    --grey-dark: #4a4a4a;
    --grey-mid: #7d7d7d;
    --grey-light: #a9a9a9;
    --rule: #c9c9c9;
    --white: #ffffff;
    --photo-top: #6f8d97;
    --photo-bottom: #8c8f91;
  }
  * { margin: 0; padding: 0; box-sizing: border-box; }
  html, body { width: 1200px; height: 2984px; overflow: hidden; background: var(--white); }
  body { font-family: "Open Sans", Arial, sans-serif; color: var(--grey-dark); }

  .banner { position: relative; width: 1200px; height: 2984px; overflow: hidden; background: var(--white); }

  .top-band {
    position: absolute; left: 0; top: 0; width: 1200px; height: 34px;
    background: linear-gradient(90deg, var(--red-deep), var(--orange) 60%, var(--red));
  }

  .brand { position: absolute; left: 90px; top: 110px; }
  .brand-name { font-size: 74px; font-weight: 700; color: var(--grey-mid); line-height: 1; letter-spacing: -1px; }
  .brand-tagline { margin-top: 18px; font-size: 40px; font-weight: 400; color: var(--grey-dark); font-style: italic; }
  .brand-tagline span { color: var(--red); }

  .headline {
    position: absolute; left: 0; width: 1200px; top: 400px; text-align: center;
    font-weight: 600; color: var(--grey-dark); line-height: 1.12;
  }
  .headline .line1 { font-size: 74px; }
  .headline .line2 { font-size: 104px; }
  .headline .accent { color: var(--red); }

  .stripes { position: absolute; left: 0; top: 640px; width: 1200px; height: 340px; z-index: 2; }

  .photo {
    position: absolute; left: 0; top: 760px; width: 1200px; height: 1120px;
    background: linear-gradient(180deg, var(--photo-top) 0%, #7f9aa3 45%, var(--photo-bottom) 100%);
    clip-path: polygon(0 14%, 100% 0, 100% 100%, 0 100%);
    z-index: 1;
  }

  .sectors {
    position: absolute; left: 0; top: 1920px; width: 1200px; height: 190px;
    display: flex; justify-content: space-around; padding: 0 60px;
    border-top: 4px solid var(--rule);
  }
  .sector { width: 300px; text-align: center; padding-top: 22px; }
  .sector svg { height: 100px; width: 200px; fill: var(--grey-mid); }
  .sector-label { margin-top: 10px; font-size: 28px; font-weight: 700; color: var(--grey-dark); letter-spacing: 1px; }

  .intro {
    position: absolute; left: 60px; width: 1080px; top: 2150px;
    text-align: center; font-size: 50px; line-height: 1.42; color: var(--red);
  }
  .intro strong { font-weight: 700; }

  .rule { position: absolute; left: 40px; width: 1120px; height: 4px; background: var(--rule); }
  .rule.r1 { top: 2460px; }
  .rule.r2 { top: 2610px; }

  .contact {
    position: absolute; left: 0; width: 1200px; top: 2470px; height: 140px;
    display: flex; align-items: center; justify-content: center; gap: 40px;
    font-size: 50px; color: var(--grey-dark);
  }
  .contact-item { display: flex; align-items: center; gap: 20px; }
  .contact-item svg { width: 44px; height: 44px; stroke: var(--grey-dark); fill: none; stroke-width: 3.5; }
  .contact-divider { width: 4px; height: 90px; background: var(--rule); }

  .membership {
    position: absolute; left: 0; width: 1200px; top: 2620px; height: 220px;
    display: flex; align-items: center; justify-content: center; gap: 50px;
  }
  .member-label { font-size: 46px; color: var(--grey-dark); }
  .member-divider { width: 4px; height: 170px; background: var(--rule); }
  .member-badge { display: flex; align-items: center; gap: 28px; }
  .badge-circle { width: 160px; height: 160px; border-radius: 50%; background: var(--red); }
  .badge-name { font-size: 44px; font-weight: 600; color: var(--red); line-height: 1.1; text-transform: uppercase; width: 330px; }

  .bottom-band {
    position: absolute; left: 0; bottom: 0; width: 1200px; height: 130px;
    background: linear-gradient(90deg, var(--red-deep), var(--orange) 50%, var(--red-deep));
  }
</style>
</head>
<body>
<main class="banner">
  <div class="top-band"></div>

  <header class="brand">
    <div class="brand-name">Brindle Forge Services</div>
    <div class="brand-tagline">the solution in <span>aluminium heat treatment</span></div>
  </header>

  <h1 class="headline">
    <div class="line1">From <span class="accent">Sheet Metal</span> To</div>
    <div class="line2 accent">Large Sand Castings</div>
  </h1>

  <svg class="stripes" viewBox="0 0 1200 340" preserveAspectRatio="none" aria-hidden="true">
    <defs>
      <linearGradient id="stripeGrad" x1="0" y1="0" x2="1" y2="0">
        <stop offset="0" stop-color="#f5a080"/>
        <stop offset="0.5" stop-color="#ec4a2c"/>
        <stop offset="1" stop-color="#d81e1a"/>
      </linearGradient>
    </defs>
    <polygon points="0,120 1200,0 1200,40 0,160" fill="url(#stripeGrad)" opacity="0.55"/>
    <polygon points="420,150 1200,40 1200,140 620,200" fill="url(#stripeGrad)"/>
    <polygon points="660,210 1200,160 1200,250 860,280" fill="url(#stripeGrad)"/>
    <polygon points="900,290 1200,265 1200,320 1040,340" fill="url(#stripeGrad)" opacity="0.85"/>
  </svg>

  <div class="photo" role="img" aria-label="Photograph of a large drop bottom heat treatment furnace in a factory hall, with a staff member in a shirt and tie holding a cast aluminium part in gloved hands"></div>

  <section class="sectors">
    <div class="sector">
      <svg viewBox="0 0 200 100" aria-hidden="true">
        <path d="M20 58 L150 40 Q185 36 188 50 Q185 62 150 60 L20 62 Z"/>
        <path d="M80 50 L120 50 L70 90 L55 90 Z"/>
        <path d="M90 46 L120 46 L80 14 L68 14 Z"/>
        <path d="M20 58 L34 58 L22 36 L12 36 Z"/>
      </svg>
      <div class="sector-label">AEROSPACE</div>
    </div>
    <div class="sector">
      <svg viewBox="0 0 200 100" aria-hidden="true">
        <path d="M20 60 Q22 44 50 40 L70 22 Q78 16 100 16 L130 16 Q146 16 156 30 L166 40 Q182 44 182 60 L182 72 L20 72 Z"/>
        <circle cx="58" cy="74" r="14" fill="#ffffff"/><circle cx="58" cy="74" r="10"/>
        <circle cx="146" cy="74" r="14" fill="#ffffff"/><circle cx="146" cy="74" r="10"/>
      </svg>
      <div class="sector-label">AUTOMOTIVE</div>
    </div>
    <div class="sector">
      <svg viewBox="0 0 200 100" aria-hidden="true">
        <path d="M40 96 L40 50 L80 30 L80 50 L120 30 L120 50 L150 36 L150 4 L170 4 L170 96 Z"/>
      </svg>
      <div class="sector-label">ENGINEERING</div>
    </div>
  </section>

  <p class="intro">
    Our <strong>Capacity</strong> and <strong>Rapid Quenching</strong> drop bottom ovens deliver <strong>precise</strong> processing. <span style="color:var(--grey-dark)">We also serve the</span> <strong>leading</strong> <span style="color:var(--grey-dark)">names in aerospace, automotive and advanced engineering.</span>
  </p>

  <div class="rule r1"></div>
  <div class="contact">
    <div class="contact-item">
      <svg viewBox="0 0 44 44" aria-hidden="true"><circle cx="22" cy="22" r="18"/><ellipse cx="22" cy="22" rx="8" ry="18"/><line x1="4" y1="22" x2="40" y2="22"/></svg>
      <span>www.brindleforge-example.co.uk</span>
    </div>
    <div class="contact-divider"></div>
    <div class="contact-item">
      <svg viewBox="0 0 44 44" aria-hidden="true"><path d="M12 6 L18 6 L21 15 L16 19 Q20 27 26 29 L30 24 L38 27 L38 33 Q36 38 30 38 Q8 34 6 12 Q6 6 12 6 Z"/></svg>
      <span>+44 (0)1632 960318</span>
    </div>
  </div>
  <div class="rule r2"></div>

  <section class="membership">
    <div class="member-label">Member</div>
    <div class="member-divider"></div>
    <div class="member-badge">
      <div class="badge-circle"></div>
      <div class="badge-name">Crafted across the shires</div>
    </div>
  </section>

  <div class="bottom-band"></div>
</main>
</body>
</html>
```